Creative UI design for web application

I need a new UI design for my web application. It will be used by small and micro business owners to plan & implement growth tactics.

I've attached the current design (which I'm open to be changed) - but in particular I need to design the centre of the screen, where the work actually happens.

There needs to be place for a title (YOUR BUSINESS) and description (say 1-2 paragraphs of text) - and am happy to include icons or imagery where makes sense. It may make sense for the user to be able to upload their business logo and name, for example.

This screen will be used by the business owner to understand the real value they offer potential customers and their point of difference - why they exist and why potential customers should care.

They'll use the information they put into this screen to plan things like their messaging.

Following that, there needs to be 2 sections in the dashboard.

The first section is titled "WHO YOU ARE"

The first section will include a number of boxes that the user can input information into, as follows:

- Logo
- Business name
- Business tag line
- Business vision
- Business bio
- Brand colours (these should end up as swatches based on the colour code they enter) - the colour code for each colour swatch should also be visible.
- Key competitors
- SWOT analysis (boxes to enter their strengths, weaknesses, opportunities and threats).

The second section is titled "WHY YOU EXIST"

The second section will include a number of boxes that the user can input information (text) into, as follows:

- Who are your ideal customers?
- What problem are you trying to solve for them?
- What pain points will this remove for them?
- How do you solve it?
- How else could this problem be solved?
- Who offers these other solutions?
- Why is your solution better?
- How much does your solution cost?
- What value are you providing to justify this cost?
- How will this make their life/job easier/better?

They should be able to write a decent amount of information in the boxes.

There should ideally be a place for a description for each of these text fields (for both section 1 & 2) as well so I can give them a little bit more direction around what to put in the box. Alternatively there could be a little icon (say a question mark or "i") that they could click on to view instructions. The instructions will be around 2-4 sentences long for each text field.

You have 2 options:

a) This all needs to appear on the one screen, and the navigation needs to be visible (as per the example attached but feel free to recreate this navigation)

Note: the page can scroll below the fold - but please provide the design for the full length of the page.

b) Potentially the 2 sections could actually be in 2 different items in the menu - YOUR BUSINESS and YOUR VALUE (which would sit next to YOUR BUSINESS and before YOUR CUSTOMER in the screenshot provided). feel free to design them as 2 separate screens if you prefer.

I have attached a screenshot of the app as it stands today (screen shot 2017) which would still exist in the new design but under a different section (the learn section from the plan2 mockup attached)

I have mocked up how this new screen could look if broken into 2 and that's also attached. If you can make this come to life - and look more engaging that would be helpful! :)

Target Market(s)

Small and micro business owners

Industry/Entity Type

Marketing

Number of Pages Required

1 page

Font styles to use
Sans Serif
Other font styles liked:
• Montserrat

Colors
87cfc6
d2a4cc
ffffff
85cae6
e8e8e8
5c5c5c

Requirements
Must have
• Use of my brand colours: #cc8eb2, #76d6c8, #68c7ff as well as white and #595959. Must be visually pleasing / engaging, designed for desktop (as it's a desktop application), really easy to use / navigate.
• Use font Montserrat light & Montserrat Regular or Bold. Mostly should be Montserrat light.
Nice to have
• Would be nice to see how this would look on mobile (as the application is responsive) but this is not mandatory.
Should not have
• Should not look too corporate or dry.

```html
<!DOCTYPE html>
<html lang="en">
<head>
<meta charset="utf-8">
<title>Brightpath – Who You Are</title>
<link href="https://fonts.googleapis.com/css2?family=Montserrat:wght@300;400;600;700&display=swap" rel="stylesheet">
<style>
:root{
  --pink:#cc8eb2;
  --teal:#76d6c8;
  --blue:#68c7ff;
  --dark:#595959;
  --header:#4f4f4f;
  --grey-band:#ececec;
  --step-grey:#858585;
  --line:#d9d9d9;
  --text:#6a6a6a;
  --white:#ffffff;
}
*{box-sizing:border-box;margin:0;padding:0}
html,body{width:746px;height:1200px;overflow:hidden;background:var(--white)}
body{position:relative;font-family:"Montserrat",sans-serif;font-weight:300;color:var(--text)}
.abs{position:absolute}

/* header */
.brand-block{left:0;top:0;width:234px;height:50px;background:var(--header);display:flex;align-items:center;justify-content:flex-end;padding-right:18px;gap:6px}
.brand-name{color:var(--white);font-weight:400;font-size:15px;letter-spacing:.5px}
.brand-dot{width:6px;height:6px;border-radius:50%;background:var(--teal)}
.utility{right:97px;top:7px;font-size:7px;display:flex;gap:14px;color:#888;font-weight:400}
.utility .call{color:var(--pink)}
.utility svg{vertical-align:-1px;margin-right:2px}
.navbar{left:234px;top:25px;width:512px;height:25px;background:var(--header)}
.nav-item{position:absolute;top:25px;height:25px;line-height:25px;font-size:8px;color:var(--white);font-weight:400}
.nav-item.active{background:var(--teal);width:42px;text-align:center}
.nav-item.active::after{content:"";position:absolute;left:17px;bottom:-4px;border:4px solid transparent;border-top-color:var(--teal);border-bottom:0}
.search{left:524px;top:25px;width:125px;height:25px;background:var(--pink);clip-path:polygon(10px 0,100% 0,100% 100%,0 100%);color:var(--white);font-size:6px;line-height:25px;padding-left:16px}
.search svg{position:absolute;right:7px;top:8px}

/* hero */
.hero{left:0;top:50px;width:746px;height:174px;background:linear-gradient(100deg,#eef2f6 0%,#c9d3de 45%,#8b9aab 75%,#6c7a8a 100%)}
.hero-ground{left:0;top:196px;width:746px;height:28px;background:linear-gradient(180deg,rgba(80,92,108,0) 0%,#56616f 60%,#3f4854 100%)}
.hero-title{left:97px;top:95px;font-size:15px;color:#444;font-weight:400}
.hero-title .new{color:var(--pink);font-weight:600}
.hero-title .adv{color:var(--blue);font-weight:600}
.hero-sub{left:97px;top:116px;width:280px;font-size:8.6px;line-height:11px;color:#555;font-weight:400}
.btn-register{left:97px;top:156px;width:79px;height:18px;background:var(--pink);color:var(--white);font-size:6.5px;font-weight:600;letter-spacing:.4px;display:flex;align-items:center;justify-content:center}

/* steps */
.steps-rule{left:0;top:263px;width:746px;height:1px;background:var(--line)}
.profile-band{left:0;top:274px;width:746px;height:64px;background:var(--grey-band)}
.step{position:absolute;top:254px;width:84px;height:20px;background:var(--step-grey);color:var(--white);font-size:7.5px;font-weight:400;display:flex;align-items:center;justify-content:center;clip-path:polygon(0 0,calc(100% - 8px) 0,100% 50%,calc(100% - 8px) 100%,0 100%,8px 50%)}
.step.current{background:var(--pink)}

.client-badge{left:97px;top:284px;width:45px;height:45px;border-radius:50%;border:1.5px solid #444;background:var(--white)}
.client-name{left:152px;top:297px;font-size:9.5px;color:#444;font-weight:400;letter-spacing:.3px}
.client-mail{left:152px;top:308px;font-size:7px;color:#888;text-decoration:underline}
.social{position:absolute;top:298px;width:17px;height:17px;border-radius:50%;border:1px solid #999;background:transparent}
.social.on{background:#555;border-color:#555}
.btn-edit{left:589px;top:297px;width:60px;height:20px;background:var(--teal);color:var(--white);font-size:7px;font-weight:600;display:flex;align-items:center;justify-content:center;gap:4px;box-shadow:0 2px 0 rgba(0,0,0,.08)}

/* cards */
.card{position:absolute;border:1px solid var(--line);background:var(--white)}
.card-head{height:19px;background:var(--pink);color:var(--white);font-size:6.5px;font-weight:600;letter-spacing:.4px;line-height:19px;padding-left:7px;position:relative}
.card-head .info{position:absolute;right:0;top:0;width:19px;height:19px;background:#4a4a4a;color:var(--white);text-align:center;font-weight:700;font-size:7px;font-family:Georgia,serif}
.card-head .info.lit{color:var(--teal)}
.card-body{padding:8px 7px;font-size:6.6px;line-height:10px;color:#6e6e6e}
.card-body b{font-weight:600;color:#555}
.toolbar{height:15px;background:#f2f2f2;display:flex;align-items:center;gap:0;padding-left:4px}
.toolbar span{width:22px;text-align:center;font-size:7px;color:#555;font-weight:600;border-right:1px solid #ddd;line-height:10px}
.tooltip{left:274px;top:646px;width:164px;height:47px;background:var(--white);border:1px solid var(--teal);font-size:6.4px;line-height:8px;text-align:center;padding:8px 12px;color:#666}
.tooltip::before{content:"";position:absolute;right:76px;top:-6px;width:9px;height:9px;background:var(--white);border-left:1px solid var(--teal);border-top:1px solid var(--teal);transform:rotate(45deg)}

.btn{position:absolute;top:1110px;height:20px;color:var(--white);font-size:7px;font-weight:600;letter-spacing:.5px;display:flex;align-items:center;justify-content:center}
.btn-save{left:296px;width:79px;background:var(--teal)}
.btn-next{left:381px;width:69px;background:var(--pink)}

/* footer */
.footer{left:0;top:1160px;width:746px;height:40px;background:var(--header)}
.footer-brand{left:97px;top:1172px;color:var(--white);font-size:13px;font-weight:400;letter-spacing:.5px}
.footer-copy{left:239px;top:1176px;color:var(--white);font-size:7.5px;font-weight:400}
.to-top{left:638px;top:1174px;width:11px;height:11px;border-radius:50%;background:var(--teal)}
</style>
</head>
<body>

<header>
  <div class="abs brand-block"><span class="brand-name">BRIGHTPATH</span><span class="brand-dot"></span></div>
  <div class="abs utility">
    <span><span class="call">Call Us:</span>
      <svg width="7" height="7" viewBox="0 0 10 10"><path d="M2 1l2 2-1 1.3a6 6 0 0 0 2.7 2.7L7 6l2 2-1.2 1.4C4.8 9.3.7 5.2.6 2.2z" fill="#cc8eb2"/></svg>555 - 010 - 2040</span>
    <span><svg width="7" height="7" viewBox="0 0 10 10"><circle cx="5" cy="5" r="4.3" fill="none" stroke="#cc8eb2"/><circle cx="5" cy="4" r="1.5" fill="#cc8eb2"/></svg>My Profile</span>
    <span><svg width="7" height="7" viewBox="0 0 10 10"><path d="M3 2.5a3.5 3.5 0 1 0 4 0M5 1v4" fill="none" stroke="#cc8eb2" stroke-width="1.2"/></svg>Log out</span>
  </div>
  <nav>
    <div class="abs navbar"></div>
    <div class="nav-item active" style="left:234px">Plan</div>
    <div class="nav-item" style="left:288px">Learn</div>
    <div class="nav-item" style="left:334px">Remember</div>
    <div class="nav-item" style="left:404px">Help</div>
    <div class="nav-item" style="left:448px">Contact Us</div>
    <div class="abs search">Search...
      <svg width="8" height="8" viewBox="0 0 10 10"><circle cx="4" cy="4" r="3" fill="none" stroke="#fff" stroke-width="1.4"/><path d="M6.3 6.3L9 9" stroke="#fff" stroke-width="1.4"/></svg>
    </div>
  </nav>
</header>

<section>
  <div class="abs hero" role="img" aria-label="Photo of young plants sprouting from stacks of coins in soil"></div>
  <div class="abs hero-ground"></div>
  <h1 class="abs hero-title">Your <span class="new">New</span> Competitive <span class="adv">Advantage</span></h1>
  <p class="abs hero-sub">Have the knowledge at your fingertips to turn you, or any of your team members into a marketing expert.</p>
  <div class="abs btn-register">REGISTER NOW!</div>
</section>

<section>
  <div class="abs steps-rule"></div>
  <div class="step current" style="left:86px">Who You Are</div>
  <div class="step" style="left:168px">Why You Exist</div>
  <div class="step" style="left:250px">Your Business</div>
  <div class="step" style="left:332px">Your Products</div>
  <div class="step" style="left:414px">Your Customers</div>
  <div class="step" style="left:496px">Your Goal</div>
  <div class="step" style="left:578px">Your Plan</div>

  <div class="abs profile-band"></div>
  <div class="abs client-badge" role="img" aria-label="Client business logo"></div>
  <div class="abs client-name">Mira Holt Studio</div>
  <div class="abs client-mail">hello@miraholtstudio.com</div>
  <span class="social" style="left:493px"></span>
  <span class="social on" style="left:514px"></span>
  <span class="social" style="left:536px"></span>
  <span class="social" style="left:557px"></span>
  <div class="abs btn-edit">
    <svg width="7" height="7" viewBox="0 0 10 10"><path d="M1 9V7l5-5 2 2-5 5z" fill="none" stroke="#fff" stroke-width="1.2"/></svg>EDIT
  </div>
</section>

<main>
  <div class="card" style="left:97px;top:359px;width:269px;height:109px">
    <div class="card-head">TAG LINE<span class="info">i</span></div>
    <div class="card-body">There are many variations of passages of Lorem Ipsum available, but the majority have suffered.</div>
  </div>

  <div class="card" style="left:380px;top:359px;width:269px;height:109px;box-shadow:0 2px 4px rgba(0,0,0,.12)">
    <div class="card-head">VISION<span class="info">i</span></div>
    <div class="toolbar"><span>B</span><span style="font-style:italic;font-family:Georgia,serif">I</span><span>≡</span><span>⋮≡</span><span>≡</span><span>≡</span><span>≡</span><span>∞</span></div>
    <div class="card-body">There are <b>many</b> variations of passages of Lorem Ipsum available, but the majority <b><i>have</i></b> suffered.</div>
  </div>

  <div class="card" style="left:97px;top:483px;width:552px;height:110px">
    <div class="card-head">BIO<span class="info">i</span></div>
    <div class="card-body">There are many variations of passages of Lorem Ipsum available, but the majority have suffered alteration in some form, by injected humour, or randomised words which don't look even slightly believable. If you are going to use a passage of Lorem Ipsum, you need to be sure there isn't anything embarrassing hidden in the middle of text. All the Lorem Ipsum generators on the Internet.</div>
  </div>

  <div class="card" style="left:97px;top:608px;width:269px;height:109px">
    <div class="card-head">BRAND COLOURS<span class="info lit">i</span></div>
    <div class="card-body">There are many variations of passages of Lorem Ipsum available, but the majority have suffered alteration in some form, by injected humour, or randomised words which don't look even slightly believable. If you are going to.</div>
  </div>

  <div class="card" style="left:380px;top:608px;width:269px;height:109px">
    <div class="card-head">KEY COMPETITORS<span class="info">i</span></div>
    <div class="card-body">There are many variations of passages of Lorem Ipsum available, but the majority have suffered alteration in some form, by injected humour, or randomised words which don't look even.</div>
  </div>

  <div class="abs tooltip">There are many variations of Lorem Ipsum available, but the majority have suffered alteration in some</div>

  <div class="card" style="left:97px;top:732px;width:269px;height:110px">
    <div class="card-head">STRENGTHS<span class="info">i</span></div>
    <div class="card-body">It is a long established fact that a reader will be distracted by the readable content of a page when looking at its layout. The point of using Lorem Ipsum is that it has a more.</div>
  </div>

  <div class="card" style="left:380px;top:732px;width:269px;height:234px">
    <div class="card-head">WEAKNESSES<span class="info">i</span></div>
    <div class="card-body">There are many variations of passages of Lorem Ipsum available, but the majority have suffered alteration in some form, by injected humour, or randomised words which don't look even slightly believable. If you are going to.</div>
  </div>

  <div class="card" style="left:97px;top:857px;width:269px;height:109px">
    <div class="card-head">OPPORTUNITIES<span class="info">i</span></div>
    <div class="card-body">It is a long established fact that a reader will be distracted by the readable content of a page when looking at its layout. The point of using Lorem Ipsum is that it has a more.</div>
  </div>

  <div class="card" style="left:97px;top:981px;width:552px;height:109px">
    <div class="card-head">THREATS<span class="info">i</span></div>
    <div class="card-body">There are many variations of passages of Lorem Ipsum available, but the majority have suffered alteration in some form, by injected humour, or randomised words which don't look even slightly believable. If you are going to use a passage of Lorem Ipsum.</div>
  </div>

  <div class="btn btn-save">SAVE CHANGES</div>
  <div class="btn btn-next">NEXT</div>
</main>

<footer>
  <div class="abs footer"></div>
  <div class="abs footer-brand">BRIGHTPATH</div>
  <div class="abs footer-copy">© 2017 Brightpath. All Right Reserved</div>
  <svg class="abs" style="left:638px;top:1174px" width="11" height="11" viewBox="0 0 11 11"><circle cx="5.5" cy="5.5" r="5.5" fill="#76d6c8"/><path d="M5.5 8.5V3M3 5.5l2.5-2.5L8 5.5" fill="none" stroke="#4f4f4f" stroke-width="1.3"/></svg>
</footer>

</body>
</html>
```